Personal Training Business Card Design

I have just started my own personal training business called "Lana Corvell Fitness". My goal as a personal trainer is to motivate, inspire and educate all of my clients about the benefits of regular exercise, nourishing the body with nutritious foods and living healthy. I train both men and women, so I would like a business card that will appeal to both sexes and not come across too feminine or too masculine. I'm looking for a fresh, yet simple look which uses "fresh" colours such as green, white and grey - similar to my logo (but open to other effective gender-neutral colour schemes). I am open to using the logo I have uploaded as one image together, or separating the text and image (also supplied).
Industry/Entity Type
Personal Trainer
Contact Information for Business Card
Lana Corvell
Fitness Coach
Address: Ground Floor, Maplewick House, 342 Larkin St, Brisbane City, 4000
Email: lanacorvellfitness@mailorbit.net
Phone: 0455 293 604
Facebook: www.socialnook.net/lanacorvellfitness
Look and feel

```html
<!DOCTYPE html>
<html lang="en">
<head>
<meta charset="utf-8">
<title>Lana Corvell Fitness – Business Card</title>
<link rel="stylesheet" href="https://fonts.googleapis.com/css2?family=Work+Sans:wght@300;400&display=swap">
<style>
  :root {
    --lime: #7fff00;
    --white: #ffffff;
    --slate: #7b8a93;
    --ink: #6f7d86;
  }
  * { margin: 0; padding: 0; box-sizing: border-box; }
  html, body { width: 998px; height: 1200px; overflow: hidden; background: var(--white); }
  .card {
    position: relative;
    width: 998px;
    height: 1200px;
    font-family: "Work Sans", "Helvetica Neue", Arial, sans-serif;
    font-weight: 300;
    color: var(--ink);
  }
  .card-front {
    position: absolute;
    inset: 0 0 auto 0;
    height: 616px;
    background: var(--lime);
  }
  .brand-disc {
    position: absolute;
    left: 339px;
    top: 63px;
    width: 320px;
    height: 320px;
    border-radius: 50%;
    background: var(--white);
  }
  .brand-name {
    position: absolute;
    left: 0;
    right: 0;
    top: 434px;
    text-align: center;
    font-size: 60px;
    font-weight: 300;
    letter-spacing: 0;
    color: var(--slate);
    line-height: 1;
    white-space: nowrap;
  }
  .tagline {
    position: absolute;
    left: 0;
    right: 0;
    top: 498px;
    text-align: center;
    font-size: 44px;
    font-weight: 300;
    color: var(--white);
    line-height: 1;
    white-space: nowrap;
  }
  .card-back { position: absolute; inset: 616px 0 0 0; }
  .back-disc {
    position: absolute;
    left: 622px;
    top: 60px;
    width: 320px;
    height: 320px;
    border-radius: 50%;
    background: var(--lime);
    display: flex;
    align-items: center;
    justify-content: center;
    text-align: center;
    font-size: 30px;
    font-weight: 300;
    line-height: 1.15;
    color: var(--white);
  }
  .contact-item {
    position: absolute;
    left: 62px;
    display: flex;
    align-items: flex-start;
    gap: 6px;
    font-size: 31px;
    line-height: 38px;
    color: var(--ink);
    white-space: nowrap;
  }
  .contact-icon {
    flex: none;
    width: 42px;
    height: 42px;
    margin-top: -2px;
    border-radius: 50%;
    background: var(--lime);
    display: flex;
    align-items: center;
    justify-content: center;
  }
  .contact-icon svg { width: 22px; height: 22px; }
  .contact-address { font-style: normal; }
  .address { top: 156px; }
  .email { top: 349px; }
  .phone { top: 425px; }
  .social { top: 502px; }
</style>
</head>
<body>
<main class="card">
  <section class="card-front">
    <div class="brand-disc"></div>
    <h1 class="brand-name">LANACORVELLFITNESS</h1>
    <p class="tagline">train smart, live strong</p>
  </section>

  <section class="card-back">
    <div class="back-disc">LANA CORVELL<br>FITNESS</div>

    <div class="contact-item address">
      <span class="contact-icon">
        <svg viewBox="0 0 24 24" fill="none" stroke="#fff" stroke-width="2.4" stroke-linejoin="round">
          <path d="M3 12 L12 4 L21 12"/><path d="M6 10 V20 H18 V10"/><path d="M10 20 V14 H14 V20"/>
        </svg>
      </span>
      <address class="contact-address">Ground Floor<br>Maplewick House<br>342 Larkin Street<br>Brisbane City 4000</address>
    </div>

    <div class="contact-item email">
      <span class="contact-icon">
        <svg viewBox="0 0 24 24" fill="none" stroke="#fff" stroke-width="2.2" stroke-linejoin="round">
          <rect x="3" y="6" width="18" height="12"/><path d="M3 6 L12 13 L21 6"/>
        </svg>
      </span>
      <span>lanacorvellfitness@mailorbit.net</span>
    </div>

    <div class="contact-item phone">
      <span class="contact-icon">
        <svg viewBox="0 0 24 24" fill="none" stroke="#fff" stroke-width="2.2" stroke-linejoin="round">
          <rect x="7" y="3" width="10" height="18" rx="2"/><circle cx="12" cy="17" r="1" fill="#fff"/>
        </svg>
      </span>
      <span>0455 293 604</span>
    </div>

    <div class="contact-item social">
      <span class="contact-icon"></span>
      <span>www.socialnook.net/lanacorvellfitness</span>
    </div>
  </section>
</main>
</body>
</html>
```